Mirelo Japanese Restaurant

We just want the japanese sakura background and the menu as below

Side dish :
Edamame $4
Japanese Steam Green Bean
Crab Craw $3 each
With Japanese mayo
Teriyaki Chicken stick $3 each
Chicken stick with home made teriyaki sauce
Tempura Prawns $7
With Japanese mayo
Miso Soup $3
Traditional Japanese soup
Salt and Pepper Calamari $7
With japanese mayo

Main dish:
Gyu Don $12
Bowl of steam rice topped with beef and onion simmered in a mildly sweet sauce.
Teriyaki Don $12
Bowl of steam rice topped with your choice of beef, chicken or pork and with our special Teriyaki sauce.
Vege Don $12
Bowl of steam rice with seasonal Vegetables with the special japanese sweet soy sauce.
Japanese Curry $12,(prawns $14)
Bowl of steam rice with Chicken, pork or prawn with japanese mild curry sauce.
Katsu Don $12
Bowl of steam rice topped with a deep-fried pork cutlet and egg with the japanese special sauce.
Oyako Don $12
Bowl of steam rice topped with chick and egg with japanese special sauce.
Spice Don $12
Bowl of steam rice topped with beef or chicken with japanese spice sauce.
Gingle Don $12
Bowl of steam rice topped with beef or chicken with japanese ginger sauce.
Sushi $3
Roll everyday on seasonal
ingredient.

Japanese-style sweets
Black Sesame Ice cream $4.5
Green tea Ice cream $4.5

```html
<!DOCTYPE html>
<html lang="en">
<head>
<meta charset="utf-8">
<title>Mirelo Japanese Restaurant – Menu</title>
<link rel="stylesheet" href="https://fonts.googleapis.com/css2?family=Alegreya+Sans:ital,wght@0,400;0,700;1,400&family=Kalam:wght@400&display=swap">
<style>
  :root {
    --backdrop: #141414;
    --pink-page: #f7d9e1;
    --pink-band: #efb3c3;
    --pink-soft: #fbe8ee;
    --white-column: #ffffff;
    --blossom: #f2a9bf;
    --branch: #b9a9ad;
    --magenta: #d3168a;
    --ink: #1c1c1c;
    --grey-name: #7b7b7b;
    --banner: rgba(250, 236, 240, 0.9);
  }
  * { box-sizing: border-box; margin: 0; padding: 0; }
  html, body {
    width: 1200px; height: 1000px; overflow: hidden;
    background: var(--backdrop);
  }
  .canvas { position: relative; width: 1200px; height: 1000px; }

  .sheet {
    position: absolute; top: 90px; width: 560px; height: 820px;
    overflow: hidden; background: var(--pink-page);
  }
  .sheet--cover { left: 30px; }
  .sheet--menu  { left: 610px; }

  /* Cover */
  .cover__band { position: absolute; top: 0; bottom: 0; background: var(--pink-band); }
  .cover__band--left  { left: 0; width: 86px; }
  .cover__band--right { right: 0; width: 70px; opacity: .7; }
  .cover__sakura {
    position: absolute; inset: 0;
    background:
      radial-gradient(ellipse 60% 30% at 30% 70%, rgba(242,169,191,.75), transparent 70%),
      radial-gradient(ellipse 55% 22% at 65% 42%, rgba(242,169,191,.6), transparent 70%),
      radial-gradient(ellipse 40% 18% at 25% 12%, rgba(185,169,173,.45), transparent 70%),
      linear-gradient(160deg, transparent 40%, rgba(185,169,173,.25) 75%, transparent 95%);
  }
  .cover__banner {
    position: absolute; left: 80px; right: 30px; top: 180px; height: 92px;
    background: var(--banner);
    border-top: 1px solid rgba(185,169,173,.6);
    border-bottom: 1px solid rgba(185,169,173,.6);
    display: flex; align-items: center;
  }
  .brand__mark {
    width: 56px; height: 56px; border-radius: 50%;
    background: var(--pink-band); margin: 0 18px 0 22px; flex: none;
  }
  .brand__name {
    font-family: "Alegreya Sans", sans-serif; font-weight: 700;
    color: var(--grey-name); font-size: 26px; line-height: 1.15;
    letter-spacing: .5px; flex: 1;
  }
  .cover__branch-art {
    width: 78px; height: 80px; margin-right: 6px; flex: none;
    border-left: 1px solid rgba(185,169,173,.7);
    background: linear-gradient(150deg, var(--pink-soft), #dcc9ce);
  }

  /* Menu page */
  .menu__photo-column { position: absolute; left: 0; top: 0; bottom: 0; width: 208px; background: var(--pink-page); }
  .menu__text-column  { position: absolute; left: 208px; top: 0; bottom: 0; width: 282px; background: var(--white-column); }
  .menu__band         { position: absolute; right: 0; top: 0; bottom: 0; width: 70px; background: var(--pink-band); opacity: .75; }
  .menu__sakura {
    position: absolute; inset: 0;
    background:
      radial-gradient(ellipse 30% 20% at 85% 38%, rgba(242,169,191,.35), transparent 70%),
      radial-gradient(ellipse 30% 18% at 80% 82%, rgba(242,169,191,.35), transparent 70%),
      radial-gradient(ellipse 25% 10% at 60% 3%, rgba(242,169,191,.3), transparent 70%);
  }
  .photo {
    position: absolute; left: 22px; width: 172px; height: 172px;
    box-shadow: 0 2px 5px rgba(0,0,0,.35);
  }
  .photo--gyu     { top: 22px;  background: radial-gradient(circle at 50% 45%, #c98a3e 0 42%, #a63a21 55%, #b51f1f 68%, #3a2a22 100%); }
  .photo--curry   { top: 214px; background: radial-gradient(circle at 50% 50%, #e3a048 0 40%, #c4541f 55%, #c3201b 70%, #5a4a3e 100%); }
  .photo--teriyaki{ top: 406px; background: radial-gradient(circle at 50% 45%, #6a2f1d 0 40%, #9b4b25 55%, #c1201c 70%, #4a3a32 100%); }
  .photo--vege    { top: 598px; background: radial-gradient(circle at 50% 45%, #d9703a 0 38%, #b98a52 52%, #c7221c 68%, #f1dede 100%); }

  .menu__content {
    position: absolute; left: 222px; top: 24px; width: 262px;
    font-family: "Alegreya Sans", sans-serif; color: var(--ink);
  }
  .menu__heading {
    font-family: "Kalam", cursive; font-weight: 400;
    color: var(--magenta); font-size: 30px; line-height: 1; margin-bottom: 6px;
  }
  .menu__section + .menu__section { margin-top: 16px; }
  .menu__item { margin-left: 6px; margin-bottom: 4px; font-size: 11.5px; line-height: 1.2; }
  .menu__item-name { font-weight: 700; }
  .menu__item-price { font-style: italic; font-weight: 400; }
  .menu__item-desc { display: block; font-style: italic; }
  .menu__section--sweets { margin-top: 22px; }
</style>
</head>
<body>
<main class="canvas">

  <section class="sheet sheet--cover" aria-label="Menu cover">
    <div class="cover__band cover__band--left"></div>
    <div class="cover__band cover__band--right"></div>
    <div class="cover__sakura" role="img" aria-label="Cherry blossom branches spreading across the cover"></div>
    <div class="cover__banner">
      <span class="brand__mark"></span>
      <h1 class="brand__name">Mirelo<br>Japanese Restaurant</h1>
      <div class="cover__branch-art" role="img" aria-label="Small cherry blossom branch sketch"></div>
    </div>
  </section>

  <section class="sheet sheet--menu" aria-label="Menu">
    <div class="menu__photo-column"></div>
    <div class="menu__text-column"></div>
    <div class="menu__band"></div>
    <div class="menu__sakura" role="img" aria-label="Faint cherry blossom sprays in the background"></div>

    <div class="photo photo--gyu" role="img" aria-label="Photo of a beef and onion rice bowl"></div>
    <div class="photo photo--curry" role="img" aria-label="Photo of Japanese curry with tempura prawn"></div>
    <div class="photo photo--teriyaki" role="img" aria-label="Photo of a teriyaki rice bowl with sesame"></div>
    <div class="photo photo--vege" role="img" aria-label="Photo of a seasonal vegetable rice bowl"></div>

    <div class="menu__content">
      <div class="menu__section">
        <h2 class="menu__heading">Side dish</h2>
        <p class="menu__item"><span class="menu__item-name">Edamame</span> <span class="menu__item-price">$4</span><span class="menu__item-desc">Japanese Steam Green Bean</span></p>
        <p class="menu__item"><span class="menu__item-name">Crab Craw</span> <span class="menu__item-price">$3 each</span><span class="menu__item-desc">With Japanese mayo</span></p>
        <p class="menu__item"><span class="menu__item-name">Teriyaki Chicken Stick</span> <span class="menu__item-price">$3 each</span><span class="menu__item-desc">Chicken stick with home made teriyaki sauce</span></p>
        <p class="menu__item"><span class="menu__item-name">Tempura Prawns</span> <span class="menu__item-price">$7</span><span class="menu__item-desc">With Japanese mayo</span></p>
        <p class="menu__item"><span class="menu__item-name">Miso Soup</span> <span class="menu__item-price">$3</span><span class="menu__item-desc">Traditional Japanese soup</span></p>
        <p class="menu__item"><span class="menu__item-name">Salt and Pepper Calamari</span> <span class="menu__item-price">$7</span><span class="menu__item-desc">With japanese mayo</span></p>
      </div>

      <div class="menu__section">
        <h2 class="menu__heading">Main dish</h2>
        <p class="menu__item"><span class="menu__item-name">Gyu Don</span> <span class="menu__item-price">$12</span><span class="menu__item-desc">Bowl of steam rice topped with beef and onion simmered in a mildly sweet sauce.</span></p>
        <p class="menu__item"><span class="menu__item-name">Teriyaki Don</span> <span class="menu__item-price">$12</span><span class="menu__item-desc">Bowl of steam rice topped with your choice of beef, chicken or pork and with our special Teriyaki sauce.</span></p>
        <p class="menu__item"><span class="menu__item-name">Vege Don</span> <span class="menu__item-price">$12</span><span class="menu__item-desc">Bowl of steam rice with seasonal vegetables with the special Japanese sweet soy sauce.</span></p>
        <p class="menu__item"><span class="menu__item-name">Japanese Curry</span> <span class="menu__item-price">$12,(prawns $14)</span><span class="menu__item-desc">Bowl of steam rice with chicken, pork or prawn with Japanese mild curry sauce.</span></p>
        <p class="menu__item"><span class="menu__item-name">Katsu Don</span> <span class="menu__item-price">$12</span><span class="menu__item-desc">Bowl of steam rice topped with a deep-fried pork cutlet and egg with the Japanese special sauce.</span></p>
        <p class="menu__item"><span class="menu__item-name">Oyako Don</span> <span class="menu__item-price">$12</span><span class="menu__item-desc">Bowl of steam rice topped with chick and egg with Japanese special sauce.</span></p>
        <p class="menu__item"><span class="menu__item-name">Spice Don</span> <span class="menu__item-price">$12</span><span class="menu__item-desc">Bowl of steam rice topped with beef or chicken with Japanese spice sauce.</span></p>
        <p class="menu__item"><span class="menu__item-name">Gingle Don</span> <span class="menu__item-price">$12</span><span class="menu__item-desc">Bowl of steam rice topped with beef or chicken with Japanese ginger sauce.</span></p>
        <p class="menu__item"><span class="menu__item-name">Sushi</span> <span class="menu__item-price">$3</span><span class="menu__item-desc">Roll everyday on seasonal ingredient.</span></p>
      </div>

      <div class="menu__section menu__section--sweets">
        <h2 class="menu__heading">Japanese-style sweets</h2>
        <p class="menu__item"><span class="menu__item-name">Black Sesame Ice cream</span> <span class="menu__item-price">$4.5</span></p>
        <p class="menu__item"><span class="menu__item-name">Green Tea Ice cream</span> <span class="menu__item-price">$4.5</span></p>
      </div>
    </div>
  </section>

</main>
</body>
</html>
```